Disability and mental health support work company requires business card

Specialising
Wrenfield Disability is a new QCAP service aimed toward QCAP participants with a history of criminal justice, psychosocial/mental health, intellectual, and cognitive disabilities.

Our focus
Focusing on providing core QCAP supports for community participation, daily activities and supported independent living.

Authentic
Likeminded people wanting to make a difference in participant's lives.

Our aim to provide holistic and empowering supports targeted towards creating independence and guidance for all participants and families.
Over 35 years of experience working with people that have psychosocial, intellectual, and cognitive disabilities.

Industry/Entity Type

disability and mental health

Contact Information for Business Card

logo - business name

Colors
0054AA
0677BA
7BADD7
CADEEF
E8F1F8
FFF300
FFF600
FEFA6F
FFFEC7
FFFEE8

Requirements
Must have
• want double sided business cards(wont let me change it)
Should not have
• any disability related pictures

```html
<!DOCTYPE html>
<html lang="en">
<head>
<meta charset="utf-8">
<title>Wrenfield Disability – Business Card</title>
<link rel="stylesheet" href="https://fonts.googleapis.com/css2?family=DM+Serif+Display&family=Mulish:wght@400;600;700&display=swap">
<style>
  :root {
    --navy: #16375e;
    --sky: #5f96d2;
    --sun: #e8b22b;
    --paper: #ffffff;
    --backdrop: #e3e0e1;
    --serif: "DM Serif Display", Georgia, serif;
    --sans: "Mulish", Arial, sans-serif;
  }
  * { box-sizing: border-box; margin: 0; padding: 0; }
  html, body { width: 1200px; height: 900px; overflow: hidden; }
  body { background: var(--backdrop); position: relative; font-family: var(--sans); }

  .card { position: absolute; width: 489px; height: 281px; left: 349px; overflow: hidden; }
  .card--front { top: 139px; background: var(--paper); }
  .card--back { top: 481px; background: var(--navy); }

  .front__rule { position: absolute; left: 0; right: 0; top: 96px; height: 1.5px; background: var(--sky); }

  .brand-disc {
    position: absolute; left: 30px; top: 19px; width: 156px; height: 156px;
    border-radius: 50%; background: var(--navy); border: 3px solid var(--sky);
    display: flex; align-items: center; justify-content: center; text-align: center;
  }
  .brand-name {
    font-family: var(--sans); font-weight: 700; color: var(--sky);
    font-size: 15px; line-height: 1.25; letter-spacing: 2px; text-transform: uppercase;
  }

  .holder { position: absolute; right: 25px; top: 42px; text-align: right; }
  .holder__name { font-family: var(--serif); color: var(--navy); font-size: 25px; line-height: 1; letter-spacing: 0.3px; }
  .holder__role { font-family: var(--sans); color: var(--sky); font-size: 13.5px; letter-spacing: 1.2px; margin-top: 3px; }

  .contacts { position: absolute; right: 25px; top: 106px; list-style: none; }
  .contacts li { display: flex; align-items: center; justify-content: flex-end; gap: 8px; height: 20px; color: var(--navy); font-size: 13.2px; letter-spacing: 0.2px; }
  .contacts svg { width: 16px; height: 16px; flex: none; }

  .address { position: absolute; left: 29px; top: 199px; color: var(--navy); font-size: 13.2px; line-height: 20px; font-style: normal; letter-spacing: 0.2px; }

  .experience-badge {
    position: absolute; left: 398px; top: 197px; width: 71px; height: 90px;
    background: var(--sun); border-radius: 36px 36px 0 0;
    display: flex; flex-direction: column; align-items: center; padding-top: 18px;
    color: var(--navy); text-align: center;
  }
  .experience-badge__figure { font-family: var(--serif); font-size: 15px; line-height: 1; }
  .experience-badge__label { font-family: var(--serif); font-size: 9px; line-height: 1.1; }
  .experience-badge__note { font-size: 5.5px; letter-spacing: 0.8px; margin-top: 4px; font-weight: 700; text-transform: uppercase; }

  .back__ring {
    position: absolute; left: 158px; top: 53px; width: 172px; height: 172px;
    border-radius: 50%; border: 2px solid #cfd6de;
    display: flex; align-items: center; justify-content: center; text-align: center;
  }
  .back__ring .brand-name { color: #cfd6de; font-size: 17px; }
  .back__url { position: absolute; left: 0; right: 0; top: 250px; text-align: center; color: var(--sky); font-size: 12px; letter-spacing: 3.6px; }
</style>
</head>
<body>
  <section class="card card--front">
    <div class="front__rule"></div>
    <div class="brand-disc"><span class="brand-name">Wrenfield<br>Disability</span></div>

    <header class="holder">
      <h1 class="holder__name">DANIEL HARPER</h1>
      <p class="holder__role">MANAGING DIRECTOR</p>
    </header>

    <ul class="contacts">
      <li>555 014 2290
        <svg viewBox="0 0 16 16"><circle cx="8" cy="8" r="8" fill="#e8b22b"/><path d="M5.4 4.2l1.4 1.6-.7 1.1c.5 1.2 1.4 2.1 2.6 2.6l1.1-.7 1.6 1.4-.9 1.2c-3-.4-5.2-2.6-5.6-5.6z" fill="none" stroke="#fff" stroke-width="1.1" stroke-linejoin="round"/></svg>
      </li>
      <li>Daniel@wrenfielddisability.com
        <svg viewBox="0 0 16 16"><circle cx="8" cy="8" r="8" fill="#e8b22b"/><rect x="4" y="5.2" width="8" height="5.6" rx="0.6" fill="none" stroke="#fff" stroke-width="1.1"/><path d="M4.3 5.6L8 8.4l3.7-2.8" fill="none" stroke="#fff" stroke-width="1.1"/></svg>
      </li>
      <li>www.wrenfielddisability.com
        <svg viewBox="0 0 16 16"><circle cx="8" cy="8" r="8" fill="#e8b22b"/><g fill="none" stroke="#fff" stroke-width="0.9"><circle cx="8" cy="8" r="4.2"/><ellipse cx="8" cy="8" rx="1.8" ry="4.2"/><path d="M3.8 8h8.4M4.4 6h7.2M4.4 10h7.2"/></g></svg>
      </li>
    </ul>

    <address class="address">118 Alder Street NW<br>Suite 210, Millbrook<br>MI 49021</address>

    <div class="experience-badge">
      <span class="experience-badge__figure">35</span>
      <span class="experience-badge__label">YEARS</span>
      <span class="experience-badge__note">of experience</span>
    </div>
  </section>

  <section class="card card--back">
    <div class="back__ring"><span class="brand-name">Wrenfield<br>Disability</span></div>
    <p class="back__url">WWW.WRENFIELDDISABILITY.COM</p>
  </section>
</body>
</html>
```